Coffee and fruit juice

We are a malaysian restaurant that also serves aussie coffee and breakfast from 7am to 11am. After 11am we serve malaysian food but we also have a salad and sandwhich bar for people to choose from. We need a poster to hang outside our door to let people know that we are now also serving aussie coffee and breakfast as well as our usual malaysian cuisine.

Target Market(s)

Office location

Industry/Entity Type

Restaurant

Font styles to use
Decorative
Script

Requirements
Must have
• images and word
Nice to have
• something bold to attract people's attention

```html
<!DOCTYPE html>
<html lang="en">
<head>
<meta charset="utf-8">
<title>Aussie Coffee and Brekkie – Served Daily 7-11AM</title>
<link rel="stylesheet" href="https://fonts.googleapis.com/css2?family=Noto+Sans:wght@700&display=swap">
<style>
  :root {
    --sign-yellow: #f5b324;
    --sign-black: #000000;
    --silhouette: #111111;
    --page-bg: #ffffff;
  }
  html, body {
    margin: 0;
    padding: 0;
    width: 1200px;
    height: 1200px;
    overflow: hidden;
    background: var(--page-bg);
  }
  .poster {
    display: block;
    width: 1200px;
    height: 1200px;
  }
  .sign-face {
    fill: var(--sign-yellow);
    stroke: var(--sign-black);
    stroke-width: 2;
    stroke-linejoin: round;
  }
  .sign-border {
    fill: none;
    stroke: var(--sign-black);
    stroke-width: 17;
    stroke-linejoin: round;
  }
  .sign-text {
    font-family: "Noto Sans", sans-serif;
    font-weight: 700;
    fill: var(--sign-black);
    text-anchor: middle;
  }
  .headline { font-size: 56px; }
  .hours { font-size: 60px; }
  .kangaroo-area {
    fill: var(--silhouette);
  }
</style>
</head>
<body>
<svg class="poster" viewBox="0 0 1060 1060" xmlns="http://www.w3.org/2000/svg">
  <!-- Diamond road sign -->
  <path class="sign-face"
        d="M530 12 Q538 12 546 20 L1040 514 Q1048 522 1048 530 Q1048 538 1040 546 L546 1040 Q538 1048 530 1048 Q522 1048 514 1040 L20 546 Q12 538 12 530 Q12 522 20 514 L514 20 Q522 12 530 12 Z"/>
  <path class="sign-border"
        d="M530 38 Q538 38 545 45 L1015 515 Q1022 522 1022 530 Q1022 538 1015 545 L545 1015 Q538 1022 530 1022 Q522 1022 515 1015 L45 545 Q38 538 38 530 Q38 522 45 515 L515 45 Q522 38 530 38 Z"/>

  <!-- Headline -->
  <text class="sign-text headline" x="532" y="207">AUSSIE</text>
  <text class="sign-text headline" x="532" y="274">COFFEE</text>
  <text class="sign-text headline" x="532" y="340">and BREKKIE</text>

  <!-- Silhouette area -->
  <rect class="kangaroo-area" x="300" y="368" width="450" height="275" rx="14"
        role="img" aria-label="Black silhouette of a kangaroo leaping to the right"/>

  <!-- Serving hours -->
  <text class="sign-text hours" x="538" y="726">SERVED</text>
  <text class="sign-text hours" x="538" y="797">DAILY</text>
  <text class="sign-text hours" x="538" y="870">7-11AM</text>
</svg>
</body>
</html>
```